Engineering Consultant Business Card

I'm starting a new business as a high-end engineering consultant in a niche field. I've attached the jpg for my logo plus the branding guideline document that I've been following. You can see my business website here: www.tarvikworks.com
I'd like a business card that has the logo on one side, then the other side has (in any order): Tarvik Works, Inc.
Dana Whitlock
President and Chief EMC Engineer
www.tarvikworks.com
dana@tarvikworks.com
Optional: motto "We will solve your EMC problems as early as possible—ideally before they even start."
I'm not planning on including a phone number
Target Market(s)
Businesses, especially makers of electronics hardware
Industry/Entity Type
Electrical engineering
Contact Information for Business Card
Company name, my name, website, email

```html
<!DOCTYPE html>
<html lang="en">
<head>
<meta charset="utf-8">
<title>Tarvik Works, Inc. — Business Card</title>
<link rel="stylesheet" href="https://fonts.googleapis.com/css2?family=Figtree:wght@400;500;700;800&display=swap">
<style>
  :root {
    --backdrop: #d3d4d6;
    --brand-blue: #2a41a0;
    --brand-blue-light: #3150ad;
    --accent-cyan: #5fc5d6;
    --ink: #1e1e22;
    --paper: #ffffff;
  }
  * { box-sizing: border-box; margin: 0; padding: 0; }
  html, body {
    width: 900px; height: 1200px; overflow: hidden;
    background: var(--backdrop);
    font-family: "Figtree", sans-serif;
  }
  .card {
    position: absolute;
    left: 135px;
    width: 630px;
    height: 360px;
  }
  .card--front {
    top: 213px;
    background: linear-gradient(120deg, var(--brand-blue) 0%, var(--brand-blue-light) 100%);
  }
  .card--back {
    top: 627px;
    background: var(--paper);
  }
  .wordmark {
    position: absolute;
    display: flex;
    align-items: center;
    gap: 14px;
    font-weight: 800;
    letter-spacing: 0.5px;
    white-space: nowrap;
  }
  .wordmark__dot {
    border-radius: 50%;
    flex: none;
  }
  .card--front .wordmark {
    left: 0; right: 0; top: 130px;
    justify-content: center;
    color: var(--paper);
    font-size: 46px;
  }
  .card--front .wordmark__dot {
    width: 42px; height: 42px;
    border: 6px solid var(--paper);
  }
  .motto-band {
    position: absolute;
    left: 0; right: 0; top: 301px;
    height: 35px;
    background: var(--accent-cyan);
    color: var(--paper);
    font-weight: 700;
    font-size: 14.2px;
    line-height: 35px;
    text-align: center;
    letter-spacing: -0.1px;
  }
  .card--back .wordmark {
    left: 48px; top: 160px;
    color: var(--brand-blue);
    font-size: 27px;
    gap: 10px;
  }
  .card--back .wordmark__dot {
    width: 30px; height: 30px;
    border: 5px solid var(--brand-blue);
  }
  .divider {
    position: absolute;
    left: 315px; top: 128px;
    width: 1.5px; height: 105px;
    background: var(--ink);
  }
  .contact {
    position: absolute;
    left: 346px; top: 126px;
    color: var(--ink);
  }
  .contact__name {
    color: var(--brand-blue);
    font-weight: 700;
    font-size: 24px;
    letter-spacing: 0.2px;
    text-transform: uppercase;
    line-height: 1;
  }
  .contact__title {
    margin-top: 9px;
    font-size: 14px;
    letter-spacing: 0.3px;
  }
  .contact__list {
    list-style: none;
    margin-top: 15px;
  }
  .contact__item {
    display: flex;
    align-items: center;
    gap: 9px;
    font-size: 14.5px;
    letter-spacing: 0.4px;
    height: 24px;
  }
  .contact__icon { width: 16px; height: 16px; flex: none; }
</style>
</head>
<body>
  <section class="card card--front" aria-label="Card front">
    <div class="wordmark"><span class="wordmark__dot"></span>Tarvik Works</div>
    <p class="motto-band">We will solve your EMC problems as early as possible—ideally before they even start.</p>
  </section>

  <section class="card card--back" aria-label="Card back">
    <div class="wordmark"><span class="wordmark__dot"></span>Tarvik Works</div>
    <div class="divider"></div>
    <div class="contact">
      <h1 class="contact__name">Dana Whitlock</h1>
      <p class="contact__title">President and Chief EMC Engineer</p>
      <ul class="contact__list">
        <li class="contact__item">
          <svg class="contact__icon" viewBox="0 0 16 16" aria-hidden="true">
            <rect x="0.5" y="3" width="15" height="10.5" fill="var(--brand-blue)"/>
            <path d="M1 3.5 L8 9 L15 3.5 M1 13 L6 8 M15 13 L10 8" stroke="#fff" stroke-width="1.2" fill="none"/>
          </svg>
          dana@tarvikworks.com
        </li>
        <li class="contact__item">
          <svg class="contact__icon" viewBox="0 0 16 16" aria-hidden="true">
            <g stroke="var(--brand-blue)" stroke-width="1.3" fill="none">
              <circle cx="8" cy="8" r="7"/>
              <ellipse cx="8" cy="8" rx="3" ry="7"/>
              <path d="M1 8 H15 M2 4.5 H14 M2 11.5 H14 M8 1 V15"/>
            </g>
          </svg>
          www.tarvikworks.com
        </li>
      </ul>
    </div>
  </section>
</body>
</html>
```